RK Bastone Construction Inc.

Design a new business card for our construction company
To be removed from current card:
Delete 25 years
Delete Tenant fit up Renovations section

```html
<!DOCTYPE html>
<html lang="en">
<head>
<meta charset="utf-8">
<title>RK Bastone Construction Inc. – Business Card</title>
<link rel="stylesheet" href="https://fonts.googleapis.com/css2?family=Montserrat:wght@400;500;700;800&display=swap">
<style>
  :root {
    --backdrop: #3b3b3b;
    --card: #141414;
    --teal: #2b8c82;
    --purple: #5e3b8f;
    --silver: #cfcfcf;
    --white: #f2f2f2;
  }
  * { box-sizing: border-box; margin: 0; padding: 0; }
  html, body { width: 1200px; height: 801px; overflow: hidden; }
  body {
    background: var(--backdrop);
    font-family: "Montserrat", sans-serif;
    color: var(--white);
    position: relative;
  }
  .card {
    position: absolute;
    top: 245px;
    width: 540px;
    height: 309px;
    background: var(--card);
    border-bottom: 3px solid var(--teal);
    box-shadow: 0 14px 30px rgba(0,0,0,.45);
  }
  .card--contact { left: 40px; }
  .card--front { left: 620px; }

  /* contact side */
  .contact-brand {
    position: absolute;
    left: 34px;
    top: 118px;
    color: var(--teal);
    font-weight: 800;
    font-size: 34px;
    line-height: 1;
    letter-spacing: -0.5px;
  }
  .contact-brand small {
    display: block;
    font-weight: 800;
    font-size: 15px;
    letter-spacing: 3.2px;
    margin-top: 4px;
  }
  .contact-block {
    position: absolute;
    left: 300px;
    top: 34px;
    width: 220px;
    padding-left: 16px;
    border-left: 1px solid var(--teal);
    border-bottom: 1px solid var(--teal);
    padding-bottom: 14px;
    font-size: 11.5px;
    line-height: 1.55;
  }
  .contact-name {
    color: var(--teal);
    font-weight: 700;
    font-size: 15px;
    letter-spacing: .5px;
    margin-bottom: 4px;
  }
  .contact-address { margin-bottom: 6px; }
  .contact-list { list-style: none; }
  .contact-list li { display: flex; align-items: center; gap: 7px; }
  .contact-list svg { width: 10px; height: 10px; fill: var(--purple); flex: none; }
  .services {
    position: absolute;
    left: 0; right: 0;
    bottom: 30px;
    text-align: center;
    font-size: 13px;
    letter-spacing: .3px;
  }
  .dot { color: var(--teal); margin: 0 8px; }

  /* front side */
  .front-brand {
    position: absolute;
    left: 0; right: 0;
    top: 92px;
    text-align: center;
    color: var(--silver);
    font-weight: 800;
    font-size: 46px;
    line-height: 1;
    letter-spacing: -1px;
  }
  .front-brand small {
    display: block;
    font-size: 19px;
    letter-spacing: 5px;
    margin-top: 6px;
  }
  .sectors {
    position: absolute;
    left: 0; right: 0;
    bottom: 54px;
    text-align: center;
    font-size: 15px;
    letter-spacing: .8px;
  }
</style>
</head>
<body>
  <section class="card card--contact">
    <div class="contact-brand">RK BASTONE<small>CONSTRUCTION INC.</small></div>
    <div class="contact-block">
      <p class="contact-name">MARCO BASTONE</p>
      <p class="contact-address">1280 Westbrook Rd., Suite 200<br>Kanata, ON K2K 3T4</p>
      <ul class="contact-list">
        <li><svg viewBox="0 0 10 10"><rect x="2" y="0" width="6" height="10" rx="1"/></svg>613-555-0148</li>
        <li><svg viewBox="0 0 10 10"><path d="M2 0h2l1 3-1.5 1a6 6 0 0 0 2.5 2.5L7 5l3 1v2a2 2 0 0 1-2 2A8 8 0 0 1 0 2a2 2 0 0 1 2-2z"/></svg>613-555-0192 ext. 114</li>
        <li><svg viewBox="0 0 10 10"><path d="M0 2h10v6H0zM0 2l5 3.5L10 2" /></svg>marco@rkbastone.ca</li>
        <li><svg viewBox="0 0 10 10"><circle cx="5" cy="5" r="5"/></svg>www.rkbastone.ca</li>
      </ul>
    </div>
    <p class="services">Turn Key Operations<span class="dot">•</span>Project Management</p>
  </section>

  <section class="card card--front">
    <div class="front-brand">RK BASTONE<small>CONSTRUCTION INC.</small></div>
    <p class="sectors">OFFICE<span class="dot">•</span>RETAIL<span class="dot">•</span>INSTITUTIONAL</p>
  </section>
</body>
</html>
```